Exciting brochure for new start up in Australia (corporate mentor program)

We are setting up a program called "The Ledger Greenhouse"
The brochure will have the following sections:
Program Framework:
5 Interactive sessions with well-respected CFO (mentor)
- Driving commercial programmes and overcoming barriers
- Executing group strategy and how you can participate
- Leading a transformation
- What does the CFO define as top talent?
- Exploring the career journey to CFO
The program focuses on discussion and insights into the 4 core areas the CFO must master;
1. Strategy & Commercial
2. Operational
3. Decision Making
4. Leadership
(please draw a venn diagram (circles intersecting) using the making one circle representing each other areas noted above. At the intersection (in the middle, please place the term "CFO Success")
Participants
High calibre participants will be hand selected and assessed before joining the program to ensure a "high performance" culture is developed within the program.
As part of the program, participants will be provided with;
- Breakfast and refreshments at each session
- Opportunity to communicate directly with CFO (mentors) in a confidential environment
- Course material and other relevant reading material
- Access to a closed community for networking with other participants (online/ social)
- Access to [kvm]'s "Summit Circle" which offers recruitment services at discounted rates
- Invites to other social, educational and networking opportunities
Please see the www.kvm.com.au website for branding and logo to use on this document.
Updates
Hi all,
The project is reasonably urgent and I'm looking to review designs of the brochure as soon as possible. If you have any questions on this, please let me know.
I'm looking forward to receiving something soon.
Thanks
JT
Target Market(s)
professionals
Font styles to use
Other font styles liked:
- modern font.. corporate yet contemporary
Requirements
Must have
- ven diagram, descriptions provided, professional image, aligned to the [kvm] website
Should not have
- soft colours, missing detail

```html
<!DOCTYPE html>
<html lang="en">
<head>
<meta charset="utf-8">
<title>The Ledger Greenhouse – Brochure</title>
<link href="https://fonts.googleapis.com/css2?family=Lato:ital,wght@0,300;0,400;0,700;0,900;1,400&family=Roboto+Condensed:wght@700&display=swap" rel="stylesheet">
<style>
:root{
  --orange:#f7931e;
  --orange-deep:#e9800c;
  --orange-light:#fbb040;
  --ink:#2b2b2b;
  --dark:#262626;
  --paper:#ffffff;
  --stage:#d9d6d2;
  --body:#3a3a3a;
}
*{margin:0;padding:0;box-sizing:border-box}
html,body{width:888px;height:1200px;overflow:hidden}
body{background:var(--stage);font-family:'Lato',sans-serif;position:relative;color:var(--body)}
.sheet{position:absolute;left:102px;width:683px;height:531px;background:var(--paper);overflow:hidden;box-shadow:0 3px 10px rgba(0,0,0,.35)}
.sheet--outer{top:48px}
.sheet--inner{top:631px}
.panel{position:absolute;top:0;height:100%}
.abs{position:absolute}
.photo{position:absolute}

/* outer: about panel */
.about{left:0;width:230px;background:linear-gradient(90deg,var(--orange-deep),var(--orange-light) 90%,#f9c36a)}
.about__text{position:absolute;left:18px;top:22px;width:194px;color:#fff}
.about__text h2{font-size:14.5px;font-weight:900;color:var(--ink);margin-bottom:6px}
.about__text h3{font-size:14.5px;font-weight:700;color:var(--ink);margin-top:14px;line-height:1}
.about__text p{font-size:10.3px;line-height:1.28}
.about__photo{left:0;top:367px;width:230px;height:164px;background:linear-gradient(135deg,#f2f2f2,#9a9a9a 60%,#d8d8d8)}

/* outer: contact panel */
.contact{left:230px;width:225px;background:linear-gradient(180deg,#fafafa,#ececec)}
.contact__photo{left:0;top:0;width:225px;height:137px;background:linear-gradient(180deg,#f1f1f1,#cfcfcf 55%,#2a2a2a 80%,#777)}
.wordmark{font-family:'Lato',sans-serif;font-weight:700;color:var(--ink);letter-spacing:2px}
.contact .wordmark{position:absolute;top:194px;width:100%;text-align:center;font-size:22px}
.contact__block{position:absolute;width:100%;text-align:center;font-size:10.6px;line-height:1.3;color:#222}
.contact__block h4{color:var(--orange);font-size:10.5px;font-weight:700;margin-bottom:11px}
.contact__block b{font-weight:700}
.contact__block--syd{top:242px}
.contact__block--mel{top:378px}
.url-pill{position:absolute;left:10px;top:487px;width:206px;height:29px;border-radius:14px;background:var(--dark);color:var(--orange);font-weight:700;font-size:15px;text-align:center;line-height:29px}

/* outer: cover panel */
.cover{left:455px;width:228px;background:#f7f7f7}
.cover .wordmark{position:absolute;top:20px;left:0;width:100%;text-align:center;font-size:40px}
.cover__frame-orange{left:10px;top:88px;width:32px;height:252px;border:8px solid var(--orange);border-right:none}
.cover__frame-dark{left:196px;top:120px;width:32px;height:220px;background:var(--dark)}
.cover__photo{left:20px;top:100px;width:196px;height:232px;background:linear-gradient(160deg,#eef0f2,#aab2bc 45%,#2f3a4a 80%)}
.cover__title{position:absolute;left:0;top:342px;width:228px;height:189px;background:linear-gradient(180deg,var(--orange),var(--orange-light));text-align:center;padding-top:26px}
.cover__title .light{display:block;font-weight:300;color:#fff;font-size:40px;line-height:1.05}
.cover__title .bold{display:block;font-weight:700;color:var(--ink);font-size:35px;line-height:1.15}

/* inner */
.tab{position:absolute;top:0;height:50px;background:linear-gradient(180deg,var(--orange-light),var(--orange));border-radius:0 0 10px 10px;color:#fff;font-weight:900;text-align:center;line-height:50px}
.tab--framework{left:15px;width:210px;font-size:15px}
.tab--participants{left:10px;width:208px;font-size:20px}
.framework{left:0;width:230px}
.framework h3{position:absolute;left:18px;top:71px;font-size:15px;font-weight:700;color:#111;line-height:1.2}
.arrow-list{list-style:none}
.arrow-list li{position:relative;padding-left:11px}
.arrow-list li::before{content:"";position:absolute;left:0;top:4px;width:4px;height:4px;border-top:2px solid var(--orange);border-right:2px solid var(--orange);transform:rotate(45deg)}
.framework .arrow-list{position:absolute;left:18px;top:116px;width:196px;font-size:10px;line-height:1.2;color:#222}
.core{left:230px;width:225px;background:linear-gradient(180deg,#fafafa,#efefef)}
.core h3{position:absolute;top:24px;width:100%;text-align:center;font-family:'Roboto Condensed',sans-serif;font-size:12.5px;color:var(--orange);line-height:1.3}
.core svg{position:absolute;left:0;top:78px}
.participants{left:455px;width:228px}
.participants__intro{position:absolute;left:13px;top:77px;width:196px;font-size:11.4px;line-height:1.28;color:#333}
.callout{position:absolute;left:8px;top:197px;width:200px;height:66px;border-radius:14px;background:linear-gradient(180deg,var(--orange-light),var(--orange));color:#fff;font-weight:700;font-size:14px;line-height:1.2;padding:6px 0 0 6px}
.participants .arrow-list{position:absolute;left:13px;top:279px;width:186px;font-size:10.6px;line-height:1.32;font-style:italic;color:#333}
.url-bar{position:absolute;left:455px;top:497px;width:228px;height:34px;background:var(--dark);color:var(--orange);font-weight:700;font-size:16px;text-align:center;line-height:34px}
.team-frame-top{left:0;top:228px;width:308px;height:14px;background:var(--dark)}
.team-frame-side{left:0;top:242px;width:16px;height:289px;background:var(--dark)}
.team-frame-orange{left:96px;top:487px;width:359px;height:44px;background:var(--orange)}
.team-photo{left:18px;top:244px;width:437px;height:262px;background:linear-gradient(120deg,#e6e6e6,#8b7a68 35%,#c9c4bd 60%,#eef1f4);border:4px solid #fff}
</style>
</head>
<body>

<section class="sheet sheet--outer">
  <div class="panel about">
    <div class="about__text">
      <h2>ABOUT US</h2>
      <p>[kvm] secure the right people for your business. We specialise in executive search, selection and contract recruitment for commerce, industry and chartered/professional services.</p>
      <h3>Our Services</h3>
      <p>From career moves to securing the best talent, we create a world of possibility.</p>
      <h3>Our Team</h3>
      <p>Our people are the foundation of our success.</p>
      <h3>Why [kvm]?</h3>
      <p>Our unique approach helps us achieve great things.</p>
      <h3>Industry Specialties</h3>
      <p>Our industry focus and experience delivers consistently excellent results.</p>
    </div>
    <div class="photo about__photo" role="img" aria-label="Black and white photo of interlocking jigsaw puzzle pieces"></div>
  </div>

  <div class="panel contact">
    <div class="photo contact__photo" role="img" aria-label="Photo of two black waiting-room chairs against a white tiled wall"></div>
    <div class="wordmark">KVM</div>
    <div class="contact__block contact__block--syd">
      <h4>SYDNEY</h4>
      Address: Level 6<br>18 Harbour Lane<br>Sydney NSW<br>Australia 2000<br>
      Phone: <b>+61 2 5550 1200</b><br>Fax: <b>+61 2 5550 1299</b><br>Email: <b>hello@kvm.com.au</b>
    </div>
    <div class="contact__block contact__block--mel">
      <h4>MELBOURNE</h4>
      Address: Level 12<br>44 Yarra Terrace<br>Melbourne Vic<br>Australia 3000<br>
      Phone: <b>+61 3 5550 1340</b>
    </div>
    <div class="url-pill">www.kvm.com.au</div>
  </div>

  <div class="panel cover">
    <div class="wordmark">KVM</div>
    <div class="abs cover__frame-orange"></div>
    <div class="abs cover__frame-dark"></div>
    <div class="photo cover__photo" role="img" aria-label="Photo of business people in suits meeting around a white table, seen from above"></div>
    <h1 class="cover__title"><span class="light">The Ledger</span><span class="bold">Greenhouse</span></h1>
  </div>
</section>

<section class="sheet sheet--inner">
  <div class="panel framework">
    <div class="tab tab--framework">PROGRAM FRAMEWORK:</div>
    <h3>5 Interactive sessions with<br>well-respected CFO (mentor)</h3>
    <ul class="arrow-list">
      <li>Driving commercial programmes and overcoming barriers</li>
      <li>Executing group strategy and how you can participate</li>
      <li>Leading a transformation</li>
      <li>What does the CFO define as top talent?</li>
      <li>Exploring the career journey to CFO</li>
    </ul>
  </div>

  <div class="panel core">
    <h3>The program focuses on discussion<br>and insights into the 4 core areas<br>the CFO must master:</h3>
    <svg width="225" height="130" viewBox="0 0 225 130" aria-label="Cycle of the four core areas around CFO Success">
      <defs>
        <linearGradient id="hubFill" x1="0" y1="0" x2="0" y2="1">
          <stop offset="0" stop-color="#fbb040"/><stop offset="1" stop-color="#f7931e"/>
        </linearGradient>
        <marker id="tip" viewBox="0 0 10 10" refX="6" refY="5" markerWidth="5" markerHeight="5" orient="auto">
          <path d="M0 0 L10 5 L0 10 z" fill="#444"/>
        </marker>
      </defs>
      <g fill="none" stroke="#444" stroke-width="1.6" marker-end="url(#tip)">
        <path d="M150 18 Q168 20 172 36"/>
        <path d="M172 84 Q168 100 150 104"/>
        <path d="M76 104 Q56 100 52 84"/>
        <path d="M52 36 Q56 20 74 18"/>
      </g>
      <ellipse cx="112" cy="62" rx="46" ry="25" fill="#fff" opacity=".7"/>
      <ellipse cx="112" cy="60" rx="44" ry="23" fill="url(#hubFill)"/>
      <text x="112" y="56" text-anchor="middle" font-family="Roboto Condensed, sans-serif" font-weight="700" font-size="16" fill="#fff">CFO</text>
      <text x="112" y="74" text-anchor="middle" font-family="Roboto Condensed, sans-serif" font-weight="700" font-size="16" fill="#fff">Success</text>
      <g font-family="Lato, sans-serif" font-size="10" fill="#222" text-anchor="middle">
        <text x="112" y="14">Strategy</text>
        <text x="112" y="26">&amp; Commercial</text>
        <text x="190" y="63">Operational</text>
        <text x="112" y="106">Decision</text>
        <text x="112" y="118">Making</text>
        <text x="38" y="63">Leadership</text>
      </g>
    </svg>
  </div>

  <div class="abs team-frame-top"></div>
  <div class="abs team-frame-side"></div>
  <div class="abs team-frame-orange"></div>
  <div class="photo team-photo" role="img" aria-label="Photo of a smiling professional team talking around a laptop in a bright office"></div>

  <div class="panel participants">
    <div class="tab tab--participants">PARTICIPANTS</div>
    <p class="participants__intro">High calibre participants will be hand selected and assessed before joining the program to ensure a "high performance" culture is developed within the program.</p>
    <div class="callout">As part of the program, participants will be provided with:</div>
    <ul class="arrow-list">
      <li>Breakfast and refreshments at each session</li>
      <li>Opportunity to communicate directly with CFO (mentors) in a confidential environment</li>
      <li>Course material and other relevant reading material</li>
      <li>Access to a closed community for networking with other participants (online/ social)</li>
      <li>Access to [kvm]'s "Summit Circle" which offers recruitment services at discounted rates</li>
      <li>Invites to other social, educational and networking opportunities</li>
    </ul>
  </div>
  <div class="url-bar">www.kvm.com.au</div>
</section>

</body>
</html>
```